Classic/Royal 5 Items Black coloured Stationery Design

Hello,
I'm looking for an Elegant Stationery set consists of 5 items as the following,
1- Letterhead
2- Business Card
3- Invoice
4- CD/DVD with their Envelope Design
5- Envelope
To let the project move ahead easily, I've included a folder consists many designs I liked from various design sites and it consists of,
1- Business card
2- Corporate Identity
3- Invoice
4- Miscellanies
Inside the first three folders, you will find a folder named "Recommended", it contains designs that I like so much and hoping to have a design like them.
The "Miscellanies" folder got some designs for Inspiration.
I'm waiting for some greats designs, a joomla template designer is a bonus for me as I will need him to design the website layer soon.
Due to upload problems at ArtHerdly, I've uploaded the folder in a .rar archive at multiple site and here is the link http://zup.qx/TRALVBNE .
Thank you
Update :- You can use this alternative download link from my Google drive to download the designs
https://files.plomwex.net/file/d/7Kq2ZpR4m8sVxT1nLw9cYb3HfJd5

```html
<!DOCTYPE html>
<html lang="en">
<head>
<meta charset="utf-8">
<title>Velmont Stationery – Letterhead and Invoice</title>
<link rel="stylesheet" href="https://fonts.googleapis.com/css2?family=Cabin:wght@400;600;700&family=Arimo:wght@400;700&display=swap">
<style>
  :root {
    --backdrop: #ececec;
    --paper: #ffffff;
    --ink: #1e1e1e;
    --ink-soft: #555555;
    --ink-faint: #9a9a9a;
    --brand: #7d7d7d;
    --table-head: #2b2b2b;
    --row-alt: #ebebeb;
    --rule: #3a3a3a;
  }
  * { box-sizing: border-box; margin: 0; padding: 0; }
  html, body { width: 1200px; height: 673px; overflow: hidden; }
  body {
    position: relative;
    background: var(--backdrop);
    font-family: "Cabin", sans-serif;
    color: var(--ink);
  }
  .sheet {
    position: absolute;
    background: var(--paper);
    overflow: hidden;
  }
  .sheet > * { position: absolute; }

  /* shared header */
  .brand { display: flex; flex-direction: column; align-items: center; width: 140px; }
  .brand-mark { width: 30px; height: 30px; border: 2px solid var(--brand); margin-bottom: 10px; }
  .brand-name { font-family: "Cabin", sans-serif; font-weight: 600; font-size: 17px; color: var(--brand); line-height: 1; }
  .brand-tagline { font-size: 7.5px; color: var(--ink-faint); margin-top: 3px; }
  .sender-name { font-weight: 700; font-size: 10px; line-height: 1.1; }
  .sender-meta { font-size: 6px; line-height: 1.35; }
  .contact-divider { width: 1px; background: var(--rule); }
  .contact-meta { font-size: 5.5px; line-height: 1.5; }

  /* letterhead */
  .letterhead { left: 207px; top: 117px; width: 383px; height: 520px; }
  .letterhead .brand { left: 22px; top: 14px; }
  .letterhead .sender-name { left: 225px; top: 25px; }
  .letterhead .sender-meta { left: 225px; top: 36px; }
  .letterhead .contact-divider { left: 298px; top: 26px; height: 28px; }
  .letterhead .contact-meta { left: 306px; top: 36px; }
  .letter-text { left: 36px; width: 330px; font-size: 7px; line-height: 7.8px; font-weight: 600; }
  .letter-footer-band {
    left: 0; bottom: 0; width: 100%; height: 9px;
    background: linear-gradient(90deg, #f4f4f4 0%, #9a9a9a 50%, #3a3a3a 100%);
  }

  /* invoice */
  .invoice { left: 670px; top: 115px; width: 390px; height: 517px; font-family: "Arimo", sans-serif; }
  .invoice .brand { left: 12px; top: 16px; }
  .invoice .brand-name, .invoice .brand-tagline { font-family: "Arimo", sans-serif; font-weight: 400; }
  .invoice .sender-name { left: 199px; top: 15px; font-family: "Arimo", sans-serif; }
  .invoice .sender-meta { left: 199px; top: 27px; font-size: 7px; }
  .invoice .contact-divider { left: 292px; top: 18px; height: 28px; }
  .invoice .contact-meta { left: 302px; top: 29px; font-size: 6px; }
  .client-block { left: 41px; top: 121px; font-size: 5.5px; line-height: 7px; color: var(--ink-soft); }
  .client-block .label { color: var(--ink); font-weight: 700; }
  .invoice-total-label { left: 41px; top: 178px; font-size: 6px; font-weight: 700; }
  .invoice-total { left: 41px; top: 187px; font-size: 14px; font-weight: 700; color: #333; }
  .due-date { left: 41px; top: 211px; font-size: 5.5px; color: var(--ink-soft); }
  .due-date b { color: var(--ink); }
  .invoice-meta { right: 27px; top: 121px; text-align: right; font-size: 5.5px; line-height: 7px; color: var(--ink-faint); }
  .invoice-title { right: 27px; top: 153px; font-size: 20px; color: #333; }
  .project-name { right: 27px; top: 179px; font-size: 5.5px; font-weight: 700; color: var(--ink-soft); }

  .items-table, .totals-table { border-collapse: collapse; font-size: 5.5px; }
  .items-table { left: 41px; top: 226px; width: 322px; border: 2px solid var(--table-head); }
  .items-table th, .totals-table th { background: var(--table-head); color: #fff; font-weight: 700; text-align: left; height: 17px; padding: 0 6px; }
  .items-table td, .totals-table td { height: 17px; padding: 0 6px; color: #333; }
  .items-table tbody tr:nth-child(even) td { background: var(--row-alt); }
  .totals-table { left: 230px; top: 324px; width: 133px; border: 2px solid var(--table-head); }
  .totals-table td { background: #fff; }

  .terms-title { left: 41px; top: 397px; font-size: 5.5px; font-weight: 700; }
  .terms-text { left: 41px; top: 406px; width: 322px; font-size: 5px; line-height: 6.5px; color: var(--ink-soft); }
  .invoice-footer-band { left: 0; bottom: 0; width: 100%; height: 8px; background: linear-gradient(90deg, #9a9a9a, #2b2b2b); }
</style>
</head>
<body>

<section class="sheet letterhead" aria-label="Letterhead">
  <div class="brand">
    <div class="brand-mark"></div>
    <div class="brand-name">Velmont</div>
    <div class="brand-tagline">Hotels and General Supplies</div>
  </div>
  <div class="sender-name">Name</div>
  <div class="sender-meta">Title:xxxxxxxxxxxx<br>Address: xxxxxxxxxxxxx</div>
  <div class="contact-divider"></div>
  <div class="contact-meta">Phone :xxxxxxxxxxxxxx<br>Email : xxxxxxxxxxxxx</div>

  <p class="letter-text" style="top:135px">1420, Alder Crest Road<br>Fairview, CA 90210.</p>
  <p class="letter-text" style="top:162px">January 29th, 2011</p>
  <p class="letter-text" style="top:180px">Mr. Harwick<br>President, Harwick Youth Center<br>512 Linden Row<br>Brookfield, NY 10044</p>
  <p class="letter-text" style="top:229px">Dear Mr. Harwick:</p>
  <p class="letter-text" style="top:247px">In the first paragraph, one needs to give a brief introduction of oneself. One should also give reference to the purpose of the letter in brief.<br>The second paragraph needs to give the details of the letter and its need. This paragraph is mostly longer than the others and plays the main role in the letter. Keep the sentences short and to the point. Avoid using complex words and sentences.</p>
  <p class="letter-text" style="top:318px">The third and last paragraph is the conclusion of the letter and can be kept short.</p>
  <p class="letter-text" style="top:337px">Sincerely,</p>
  <p class="letter-text" style="top:355px">(this is where the signature of the writer will be placed)</p>
  <p class="letter-text" style="top:374px">Elena Marsh<br>Read more at Notewell: http://www.notewell-example.com/articles/letter-format-guide.html</p>
  <div class="letter-footer-band"></div>
</section>

<section class="sheet invoice" aria-label="Invoice">
  <div class="brand">
    <div class="brand-mark"></div>
    <div class="brand-name">Velmont</div>
    <div class="brand-tagline">Hotels and General Supplies</div>
  </div>
  <div class="sender-name">Name</div>
  <div class="sender-meta">Title:xxxxxxxxxxxxx<br>Address: xxxxxxxxxxxxx</div>
  <div class="contact-divider"></div>
  <div class="contact-meta">Phone :xxxxxxxxxxxxxxx<br>Email : xxxxxxxxxxxxxx</div>

  <div class="client-block"><span class="label">To:</span><br><span class="label">Client Name</span><br>Client Address Line 1<br>Address Line 2<br>City Postcode<br>Country</div>
  <div class="invoice-total-label">Invoice Total:</div>
  <div class="invoice-total">$2,500.00</div>
  <div class="due-date"><b>Due by:</b> Wed, 01 Sep 10</div>
  <div class="invoice-meta">Mon 2 Aug 2010<br>Invoice # 0001</div>
  <div class="invoice-title">Invoice</div>
  <div class="project-name">Project Name Here</div>

  <table class="items-table">
    <thead><tr><th style="width:160px">Item Description</th><th>Qty</th><th>Unit Price</th><th>VAT</th><th>Total</th></tr></thead>
    <tbody>
      <tr><td>Website Design</td><td>1</td><td>$2,000</td><td>$0</td><td>$2,000</td></tr>
      <tr><td>Domain Registration</td><td>1</td><td>$20</td><td>$0</td><td>$20</td></tr>
      <tr><td>1 Years Webhosting</td><td>1</td><td>$80</td><td>$0</td><td>$80</td></tr>
      <tr><td>E-Marketing &amp; Strategy Training</td><td>4</td><td>$100</td><td>$0</td><td>$100</td></tr>
    </tbody>
  </table>

  <table class="totals-table">
    <thead><tr><th>Sub Total</th><th>VAT</th><th>Total Due</th></tr></thead>
    <tbody><tr><td>$2,000</td><td>$0</td><td><b>$2,000</b></td></tr></tbody>
  </table>

  <div class="terms-title">Terms &amp; Conditions of Invoice</div>
  <p class="terms-text">Payment is due within thirty days of the invoice date. Late payments may incur a fee of two percent per month. Please include the invoice number with your payment and contact us with any questions about these charges or services.</p>
  <div class="invoice-footer-band"></div>
</section>

</body>
</html>
```